We need a business card design for our residential home building company based out of East Tennessee and the Smoky Mountains. We have 30 years of experience, and we plan to build homes not only in the state of Tennessee, but out of state as well. We are a different kind of production home builder; we aim to build homes cost-effectively and efficiently but with the character, dignity, and charm of historic homes. Our homes have a timeless style with modern floorplans and features. We would like to see designs that embody a classic style with accents of gold, red, and blue. The resulting business card should convey elegance, strength, character, and trust as well as the careful balance of the old and new.
Motto: "Handcrafting Your Heritage"
Target Market(s)
Adults 40+ from the Northern states looking to settle in Tennessee.
Industry/Entity Type
Residential
Contact Information for Business Card
Birchline Dwellworks, LLC
Marisol Thackett | Director of Operations
24815 Quarrybend Lane | Suite 500
Knoxville, TN 48261
Office: (555)314-2290
Mobile: (555)648-1173
Email: marisol@birchlinedwellworks.example

```html
<!DOCTYPE html>
<html lang="en">
<head>
<meta charset="utf-8">
<title>Birchline Dwellworks, LLC – Business Card</title>
<link rel="stylesheet" href="https://fonts.googleapis.com/css2?family=Open+Sans:wght@400;600;700&display=swap">
<style>
  :root {
    --backdrop: #e9e6e1;
    --cream: #fbf1d6;
    --white: #ffffff;
    --gold: #8c6a3a;
    --red: #e0262b;
    --blue: #3f7fc4;
    --grey: #9a9a9a;
    --ink: #1e1e1e;
    --brown-text: #7a5a2e;
  }
  * { margin: 0; padding: 0; box-sizing: border-box; }
  html, body { width: 1200px; height: 784px; overflow: hidden; }
  body {
    background: var(--backdrop);
    font-family: "Open Sans", Arial, sans-serif;
    position: relative;
  }
  .card {
    position: absolute;
    top: 232px;
    width: 560px;
    height: 320px;
    overflow: hidden;
    box-shadow: 0 2px 10px rgba(0,0,0,0.15);
  }
  .card--front { left: 30px; background: var(--cream); }
  .card--back { left: 610px; background: var(--white); }

  /* front */
  .front-illustration {
    position: absolute; left: 20px; top: 20px; width: 300px; height: 280px;
    border-radius: 8px;
    background: radial-gradient(circle at 45% 40%, #efd9a6 0%, #d9b877 55%, #c99a57 100%);
  }
  .front-seal {
    position: absolute; left: 360px; top: 22px; width: 100px; height: 100px;
    border-radius: 50%;
    background: radial-gradient(circle at 40% 35%, #f1d27a, #b8862b 70%, #7b5516);
  }
  .front-name {
    position: absolute; right: 24px; top: 148px; width: 230px;
    font-weight: 700; font-size: 30px; line-height: 1.1;
    color: var(--gold); text-align: right;
  }

  /* back */
  .swoosh { position: absolute; left: 0; top: 0; }
  .back-illustration {
    position: absolute; left: 70px; top: 24px; width: 130px; height: 108px;
    border-radius: 6px;
    background: radial-gradient(circle at 50% 40%, #f0dfb8 0%, #d6b67a 60%, #c49a5a 100%);
  }
  .back-name {
    position: absolute; left: 40px; top: 138px; width: 190px;
    font-weight: 700; font-size: 18px; line-height: 1.1;
    color: var(--gold); text-align: center;
  }
  .rule { position: absolute; height: 5px; }
  .rule--gold { left: 40px; top: 184px; width: 190px; background: var(--gold); }
  .rule--step-gold { left: 210px; top: 128px; width: 80px; background: var(--gold); }
  .rule--step-grey { left: 292px; top: 110px; width: 100px; background: var(--grey); }
  .rule--step-black { left: 394px; top: 74px; width: 150px; background: var(--ink); }

  .person { position: absolute; right: 18px; top: 28px; text-align: right; }
  .person__name { font-size: 17px; color: var(--brown-text); line-height: 1.2; }
  .person__title { font-size: 11px; color: var(--ink); }

  .address {
    position: absolute; right: 18px; top: 98px; text-align: right;
    font-style: normal; font-size: 12px; line-height: 1.35; color: var(--brown-text);
  }
  .address__pin { position: absolute; right: -2px; top: -16px; }

  .contacts { position: absolute; left: 36px; top: 200px; list-style: none; }
  .contacts li {
    display: flex; align-items: center; gap: 10px;
    font-size: 13px; line-height: 19px; color: var(--ink);
  }
  .contacts svg { width: 11px; height: 11px; flex: none; }
</style>
</head>
<body>
  <section class="card card--front" aria-label="Card front">
    <div class="front-illustration" role="img" aria-label="Gold engraved eagle head above red, white and blue roses"></div>
    <div class="front-seal" role="img" aria-label="Gold experience seal"></div>
    <div class="front-name">Birchline Dwellworks, LLC</div>
  </section>

  <section class="card card--back" aria-label="Card back">
    <svg class="swoosh" width="560" height="320" viewBox="0 0 560 320" aria-hidden="true">
      <path d="M0 316 C260 316 460 280 560 218 L560 320 L0 320 Z" fill="var(--gold)"/>
      <path d="M0 306 C260 306 460 270 560 208" fill="none" stroke="var(--blue)" stroke-width="8"/>
      <path d="M250 294 C390 282 480 250 560 190" fill="none" stroke="var(--red)" stroke-width="3"/>
    </svg>

    <div class="back-illustration" role="img" aria-label="Eagle head with red, white and blue roses"></div>
    <div class="back-name">Birchline Dwellworks, LLC</div>

    <div class="rule rule--gold"></div>
    <div class="rule rule--step-gold"></div>
    <div class="rule rule--step-grey"></div>
    <div class="rule rule--step-black"></div>

    <div class="person">
      <p class="person__name">Marisol Thackett</p>
      <p class="person__title">Director of Operations</p>
    </div>

    <address class="address">
      <svg class="address__pin" width="10" height="14" viewBox="0 0 10 14" aria-hidden="true">
        <path d="M5 0 C2 0 0 2.2 0 5 C0 8.5 5 14 5 14 C5 14 10 8.5 10 5 C10 2.2 8 0 5 0 Z" fill="var(--ink)"/>
        <circle cx="5" cy="5" r="2" fill="var(--white)"/>
      </svg>
      24815 Quarrybend Lane<br>
      Suite 500 Knoxville<br>
      TN 48261
    </address>

    <ul class="contacts">
      <li>
        <svg viewBox="0 0 12 12" aria-hidden="true"><path d="M1 4 C1 2 3 1 6 1 C9 1 11 2 11 4 L8 4 L8 3 L4 3 L4 4 Z M2 6 L10 6 L10 11 L2 11 Z" fill="var(--ink)"/></svg>
        (555)314-2290
      </li>
      <li>
        <svg viewBox="0 0 12 12" aria-hidden="true"><rect x="2.5" y="0.5" width="7" height="11" rx="1" fill="none" stroke="var(--ink)"/></svg>
        (555)648-1173
      </li>
      <li>
        <svg viewBox="0 0 12 12" aria-hidden="true"><rect x="0.5" y="2" width="11" height="8" fill="var(--ink)"/><path d="M0.5 2 L6 7 L11.5 2" fill="none" stroke="var(--white)"/></svg>
        marisol@birchlinedwellworks.example
      </li>
    </ul>
  </section>
</body>
</html>
```